Web Page Design for a Website that Provides Tutoring

I am looking to create an online tutoring website. The website will allow parents or students to contact tutors with a view to instructing them to tutor themselves or their children.

The name of the website is LendYourLessons.

This brief is to create the design for one of the web pages for this web site. I am hoping the same designer will be available to design other pages.

The page I want designed is one of the more complex and I have attached the design as an excel spreadsheet. The web page needs to include all the items on this page but if you want to change the positioning of the items then Im fine with that.

I recently had two logos created for this website. My favourite is the one with a mortar board but im not sure I like the colours. I have attached both of these logos and you can use either of them, change the colours or create something different. I just want a design pleasing to the eye. If the logo is changed I would like that in a seperate file.

So can you please submit designs for this page. I have attached the two logos which you can use, change or if you feel you have a better idea then you can use that.

On the spreadsheet the Send Message, Favourite etc are buttons.

Target Market(s)

People who want to better themselves.
Possible middle class to upper class.

Industry/Entity Type

Tutoring

Number of Pages Required

1 page

Requirements
Must have
• The designs must have alot of the information attached in the spreadsheet.

```html
<!DOCTYPE html>
<html lang="en">
<head>
<meta charset="utf-8">
<title>LendYourLessons – Tutor Profile</title>
<link rel="stylesheet" href="https://fonts.googleapis.com/css2?family=Cabin:wght@400;600;700&family=Lato:wght@700;900&display=swap">
<style>
:root{
  --orange:#f7941d;
  --sky:#00aeef;
  --navy:#2e5a9c;
  --heading-blue:#1b8ac4;
  --band:#dae3f7;
  --page:#efefef;
  --white:#ffffff;
  --ink:#2b2b2b;
  --grey-box:#dadada;
  --line:#d5d5d5;
  --hero-a:#1d8fc0;
  --hero-b:#0a5f8c;
}
*{box-sizing:border-box;margin:0;padding:0}
html,body{width:693px;height:1200px;overflow:hidden;background:var(--page)}
body{font-family:"Cabin",Arial,sans-serif;color:var(--ink);position:relative}
.abs{position:absolute}

/* header */
.site-header{left:0;top:0;width:693px;height:54px;background:var(--white)}
.brand{left:66px;top:12px;display:flex;align-items:center;gap:5px;font-weight:700;font-size:22px;color:var(--orange);letter-spacing:-.3px}
.brand-mark{width:14px;height:14px;background:var(--orange)}
.user-links{left:520px;top:7px;font-size:10.5px;font-weight:700;color:var(--navy);display:flex;gap:10px}
.user-links .sep{width:1px;height:13px;background:var(--navy)}
.search-input{left:448px;top:28px;width:110px;height:19px;border:1px solid #bbb;background:var(--white);font-size:7.5px;color:#777;padding:4px 7px;font-weight:600}
.search-btn{left:562px;top:27px;width:50px;height:21px;background:var(--orange);border:1px solid #d97a0c;color:var(--white);font-size:9.5px;font-weight:700;text-align:center;line-height:19px}

/* nav */
.main-nav{left:0;top:54px;width:693px;height:32px;background:var(--sky)}
.main-nav ul{list-style:none;position:absolute;left:66px;top:0;display:flex;height:32px;border-left:1px solid var(--white)}
.main-nav li{width:109.5px;height:32px;border-right:1px solid var(--white);color:var(--white);font-weight:700;font-size:11px;display:flex;align-items:center;justify-content:center;letter-spacing:.3px}
.main-nav li.active{background:var(--navy)}

/* hero */
.hero{left:0;top:86px;width:693px;height:168px;background:radial-gradient(circle at 30% 50%,var(--hero-a),var(--hero-b) 80%)}
.hero-photo{left:434px;top:86px;width:259px;height:168px;background:linear-gradient(135deg,#d8e6ee,#c9a58e 55%,#8f6a55);clip-path:ellipse(100% 100% at 100% 50%)}
.avatar{left:68px;top:132px;width:80px;height:80px;border-radius:50%;background:linear-gradient(160deg,#e7e2ee,#a88a7a);border:2px solid rgba(255,255,255,.35)}
.tutor-name{left:170px;top:143px;color:var(--orange);font-weight:700;font-size:12px}
.tutor-title{left:170px;top:162px;color:var(--white);font-size:12px;font-weight:600;letter-spacing:.3px}
.availability-status{left:170px;top:184px;display:flex;align-items:center;gap:8px;color:var(--white);font-size:12px;font-weight:600}
.toggle{width:24px;height:12px;border-radius:6px;background:#3f8f2c;position:relative}
.toggle::after{content:"";position:absolute;right:2px;top:2px;width:8px;height:8px;border-radius:50%;background:var(--white)}
.profile-tab{left:264px;top:242px;width:56px;height:18px;background:var(--page);clip-path:polygon(8% 0,92% 0,100% 100%,0 100%);font-size:7.5px;font-weight:700;color:#555;text-align:center;line-height:19px}

/* cards */
.card{background:var(--white);border:1px solid var(--line);border-radius:3px}
.price-card{left:66px;top:274px;width:180px;height:107px}
.card-band{height:27px;background:var(--band);color:var(--heading-blue);font-weight:700;font-size:10px;padding:7px 15px}
.price-tag{position:absolute;left:14px;top:42px;width:88px;height:21px;background:var(--orange);color:var(--white);font-size:10px;font-weight:600;text-align:center;line-height:21px;letter-spacing:.3px}
.social-row{position:absolute;left:14px;top:75px;display:flex;gap:3px}
.social-row span{width:11px;height:11px;background:var(--navy)}
.intro-card{left:258px;top:274px;width:354px;height:107px;padding:14px 10px}
.intro-card h2{font-size:10.5px;color:var(--heading-blue);font-weight:700;margin-bottom:6px}
.intro-card p{font-size:7.3px;line-height:10px;font-weight:600;margin-bottom:7px}
.learn-more{position:absolute;right:10px;bottom:20px;font-size:6.5px;color:var(--heading-blue);text-decoration:underline;font-weight:700}
.action-btn{top:392px;width:94px;height:22px;background:var(--orange);color:var(--white);font-size:9.5px;font-weight:600;text-align:center;line-height:22px;letter-spacing:.3px}

/* detail panels */
.panel{left:66px;width:547px;background:var(--white);border:1px solid var(--line);border-radius:3px}
.panel::before{content:"";position:absolute;left:0;top:0;width:100%;height:29px;background:var(--band)}
.col{position:absolute;top:0}
.col h3{font-size:9.3px;color:var(--heading-blue);font-weight:700;height:29px;line-height:29px;position:relative}
.col .box{position:relative;background:var(--grey-box);margin-top:4px;padding:7px 6px 0 15px;font-size:7.3px;font-weight:600;line-height:13px}
.col .box::before{content:"";position:absolute;left:6px;top:-4px;border:4px solid transparent;border-top:0;border-bottom-color:var(--grey-box)}
.col .box ul{list-style:none}
.col .box li{position:relative;min-height:13px}
.col .box li::before{content:"";position:absolute;left:-8px;top:5px;width:4px;height:4px;border-radius:50%;background:var(--orange)}
.info-panel{top:439px;height:102px}
.info-panel .box{width:90px;height:62px}
.subjects-panel{top:607px;height:101px}
.subjects-panel .box{width:73px;height:62px}

.section-title{left:65px;font-family:"Lato",Arial,sans-serif;font-weight:900;font-size:14px;color:#2a2a2a;letter-spacing:.2px}

/* tables */
.data-table{left:66px;width:547px;border-collapse:collapse;background:var(--white);border:1px solid var(--line);font-size:7.5px;font-weight:600}
.data-table th{background:var(--band);color:var(--heading-blue);font-size:9px;font-weight:700;height:28px;border-right:1px solid var(--white)}
.data-table td{border:1px solid var(--line);border-width:1px 1px 0 0}
.data-table tr.shaded td{background:var(--band)}
.availability-table{top:773px}
.availability-table td{height:23.8px}
.availability-table td:first-child{padding-left:15px}
.select{display:flex;width:51px;height:18px;border:1px solid #7a90c0;background:var(--white);margin:0 auto;align-items:center;font-size:7.5px;padding-left:9px;justify-content:space-between}
.select .arrow{width:13px;height:14px;background:#a9bde6;margin-right:1px;display:flex;align-items:center;justify-content:center}
.select .arrow::after{content:"";border:4px solid transparent;border-top:6px solid var(--navy);border-bottom:0;margin-top:2px}
.reviews-table{top:984px}
.reviews-table th{text-align:left;padding-left:15px}
.reviews-table th:nth-child(3){text-align:center;padding-left:0}
.reviews-table td{height:23.6px;padding-left:12px}
.reviews-table td.stars{color:var(--orange);font-size:9.5px;letter-spacing:-.5px;padding-left:12px}

/* footer */
.site-footer{left:0;top:1164px;width:693px;height:36px;background:var(--navy)}
.copyright{left:66px;top:1176px;color:var(--white);font-size:8.5px;font-weight:700}
.footer-social{left:526px;top:1172px;display:flex;gap:4px}
.footer-social span{width:19px;height:19px;background:var(--orange)}
</style>
</head>
<body>

<header class="site-header abs"></header>
<div class="brand abs"><span class="brand-mark"></span>LendYourLessons</div>
<div class="user-links abs"><span>Hi Jane</span><span class="sep"></span><span>Logout</span></div>
<div class="search-input abs">Subject (ex: algebra)</div>
<div class="search-btn abs">Search</div>

<nav class="main-nav abs">
  <ul>
    <li class="active">HOME</li><li>STUDENT</li><li>TUTOR</li><li>ABOUT</li><li>CONTACT</li>
  </ul>
</nav>

<section class="hero abs"></section>
<div class="hero-photo abs" role="img" aria-label="Tutor helping a group of young children with classwork"></div>
<div class="avatar abs" role="img" aria-label="Tutor portrait"></div>
<div class="tutor-name abs">Jane D.</div>
<div class="tutor-title abs">Professional English Tutor</div>
<div class="availability-status abs"><span class="toggle"></span>Jane D. is available.</div>
<div class="profile-tab abs">Profile</div>

<div class="card price-card abs">
  <div class="card-band">Piccle</div>
  <div class="price-tag">25 USD / hour</div>
  <div class="social-row"><span></span><span></span><span></span><span></span></div>
</div>

<div class="card intro-card abs">
  <h2>Introduction</h2>
  <p>My name is Jane and I am professional English tutor. This in an example profile and this is dummy content.</p>
  <p>Please contact me to discuses your goals and your availablity for lessons.</p>
  <span class="learn-more">Learn more</span>
</div>

<div class="action-btn abs" style="left:282px">Send Message</div>
<div class="action-btn abs" style="left:390px">Favour Tutor</div>
<div class="action-btn abs" style="left:497px">Write Review</div>

<section class="panel info-panel abs">
  <div class="col" style="left:36px"><h3>Tutoring type</h3><div class="box"><ul><li>In personal only</li><li>Home Only</li></ul></div></div>
  <div class="col" style="left:132px"><h3>Teacher</h3><div class="box"><ul><li>Full Time Tutor</li><li>Full Time Student</li></ul></div></div>
  <div class="col" style="left:227px"><h3>Willing to Travel</h3><div class="box"><ul><li>Yes</li><li>No</li></ul></div></div>
  <div class="col" style="left:322px"><h3>Age</h3><div class="box"><ul><li>20 years</li></ul></div></div>
  <div class="col" style="left:417px"><h3>DBS (CRB)</h3><div class="box"><ul><li></li><li></li></ul></div></div>
</section>

<h2 class="section-title abs" style="top:574px">SUBJECTS TAUGHTS</h2>
<section class="panel subjects-panel abs">
  <div class="col" style="left:36px"><h3>Primary</h3><div class="box"><ul><li>Biology £20</li><li>Chemistry £20</li></ul></div></div>
  <div class="col" style="left:116px"><h3>Secondary</h3><div class="box"><ul><li></li><li></li></ul></div></div>
  <div class="col" style="left:195px"><h3>GCSE</h3><div class="box"><ul><li>£25</li><li>£25</li></ul></div></div>
  <div class="col" style="left:275px"><h3>A-level</h3><div class="box"><ul><li>£30</li><li>£30</li></ul></div></div>
  <div class="col" style="left:354px"><h3>University</h3><div class="box"><ul><li></li><li></li></ul></div></div>
  <div class="col" style="left:434px"><h3>Adult Learner</h3><div class="box"><ul><li></li><li></li></ul></div></div>
</section>

<h2 class="section-title abs" style="top:740px">AVAILABILITY</h2>
<table class="data-table availability-table abs">
  <colgroup><col style="width:58px"><col style="width:58px"><col style="width:59px"><col style="width:62px"><col style="width:62px"><col style="width:63px"><col style="width:63px"><col style="width:61px"><col style="width:61px"></colgroup>
  <tr><th></th><th>Monday</th><th>Tuesday</th><th>Wednesday</th><th>Thursday</th><th>Friday</th><th>Saturday</th><th>Sunday</th><th></th></tr>
  <tr><td>7 to 8</td><td></td><td></td><td></td><td></td><td></td><td></td><td></td><td><div class="select">NO<span class="arrow"></span></div></td></tr>
  <tr class="shaded"><td>8 to 9</td><td></td><td></td><td></td><td></td><td></td><td></td><td></td><td><div class="select">NO<span class="arrow"></span></div></td></tr>
  <tr><td>4 to 5</td><td></td><td></td><td></td><td></td><td></td><td></td><td></td><td><div class="select">NO<span class="arrow"></span></div></td></tr>
  <tr class="shaded"><td>5 to 6</td><td></td><td></td><td></td><td></td><td></td><td></td><td></td><td><div class="select">NO<span class="arrow"></span></div></td></tr>
  <tr><td>7 to 8</td><td></td><td></td><td></td><td></td><td></td><td></td><td></td><td></td></tr>
</table>

<h2 class="section-title abs" style="top:950px">TUTOR'S NAME REVIEWS</h2>
<table class="data-table reviews-table abs">
  <colgroup><col style="width:112px"><col style="width:126px"><col style="width:71px"><col style="width:238px"></colgroup>
  <tr><th>Tutee Name</th><th>Date / Time of Review</th><th>Rating</th><th>Comments</th></tr>
  <tr><td>Nick</td><td>12 Dec 2016&nbsp; 04:30 PM</td><td class="stars">★★★★★</td><td>Thank you.</td></tr>
  <tr class="shaded"><td>Watson</td><td>12 Dec 2016&nbsp; 04:30 PM</td><td class="stars">★★★★★</td><td>Awsome Instructor.</td></tr>
  <tr><td>Bella</td><td>12 Dec 2016&nbsp; 04:30 PM</td><td class="stars">★★★★★</td><td>Very Thankful to you.</td></tr>
  <tr class="shaded"><td>Tara Swain</td><td>12 Dec 2016&nbsp; 04:30 PM</td><td class="stars">★★★★★</td><td>Thank you.</td></tr>
  <tr><td>Jack</td><td>12 Dec 2016&nbsp; 04:30 PM</td><td class="stars">★★★★★</td><td>Awsome Instructor.</td></tr>
</table>

<footer class="site-footer abs"></footer>
<div class="copyright abs">Copyright 2016.</div>
<div class="footer-social abs"><span></span><span></span><span></span><span></span></div>

</body>
</html>
```